Website Front Page Banner Design for High Technology Intellectual Property

Develop Graphical Hero Banner to be used on the main page of Velmora .com. The banner will promote the availability of Velmora JESD204C IP (Intellectual Property). Please see attached pdf doc and follow details for Static Banner. We are looking for a Banner that is visually attention grabbing and uses imagery of applications that are enabled by the IP we are promoting (Applications such as 5G Wireless Infrastructure, CT/MRI/Ultrasound medical equipment, Radar / LIDAR / Satellites and High-Speed Test and Measurement equipment for a few examples). It would be good if the banner generally follow our color template of Green, White and Black - but the images of applications can use additional colors. Additonally, to learn more about JESD204 - recommend going to the following sites to understand what this IP is used for and what markets it address - additionally, I am open to answer any questions you may have. Sites: https://www.brantwise-labs.example/blog/high-speed-interface/jesd204c/, https://resources.quorvane.example/p/what-jesd204c-standard-adcs,
Target Market(s)
Various High Technology Markets such as Defense, Medical, Test and Measurement, Industrial / Robotics, Wireless Communications
Industry/Entity Type
Semiconductor

```html
<!DOCTYPE html>
<html lang="en">
<head>
<meta charset="UTF-8">
<title>Velmora JESD204C IP – Hero Banner</title>
<link href="https://fonts.googleapis.com/css2?family=Bebas+Neue&family=Poppins:wght@400;500;600&display=swap" rel="stylesheet">
<style>
  :root {
    --bg-black: #0b0c0b;
    --bg-dark: #151716;
    --brand-green: #22c03a;
    --brand-green-bright: #2bd146;
    --text-white: #ffffff;
    --text-soft: #e8e8e8;
    --board-dark: #2a2c2b;
    --board-mid: #4a4d4b;
  }
  * { margin: 0; padding: 0; box-sizing: border-box; }
  html, body {
    width: 1200px;
    height: 600px;
    overflow: hidden;
    background: var(--bg-black);
  }
  .hero-banner {
    position: relative;
    width: 1200px;
    height: 600px;
    overflow: hidden;
    background:
      radial-gradient(ellipse at 85% 55%, rgba(255,255,255,0.06), transparent 55%),
      linear-gradient(90deg, var(--bg-black) 0%, var(--bg-dark) 60%, var(--bg-black) 100%);
    font-family: "Poppins", sans-serif;
    color: var(--text-white);
  }
  .accent-band {
    position: absolute;
    left: 126px;
    top: 0;
    width: 228px;
    height: 600px;
    background: var(--brand-green);
  }
  .product-visual {
    position: absolute;
    left: 228px;
    top: 90px;
    width: 92px;
    height: 520px;
    border-radius: 6px;
    transform: rotate(45deg);
    transform-origin: center;
    left: 200px;
    top: 40px;
    background: linear-gradient(180deg, var(--board-mid) 0%, var(--board-dark) 50%, var(--board-mid) 100%);
    box-shadow: 0 18px 30px rgba(0,0,0,0.45);
  }
  .headline {
    position: absolute;
    left: 546px;
    top: 58px;
    font-family: "Bebas Neue", sans-serif;
    font-weight: 400;
    line-height: 74px;
    font-size: 72px;
    letter-spacing: 0.5px;
    white-space: nowrap;
  }
  .headline .product-name { color: var(--brand-green-bright); display: block; }
  .headline .tagline { color: var(--text-white); display: block; }
  .feature-list {
    position: absolute;
    left: 580px;
    top: 305px;
    list-style: none;
  }
  .feature-item {
    display: flex;
    align-items: center;
    height: 48px;
    font-size: 20px;
    color: var(--text-soft);
    white-space: nowrap;
  }
  .feature-item .tick {
    width: 22px;
    height: 22px;
    margin-right: 23px;
    flex: none;
  }
  .feature-item .highlight { color: var(--brand-green-bright); }
  .cta-button {
    position: absolute;
    left: 546px;
    top: 472px;
    width: 308px;
    height: 62px;
    border-radius: 10px;
    background: var(--brand-green);
    color: var(--text-white);
    font-weight: 600;
    font-size: 20px;
    display: flex;
    align-items: center;
    justify-content: center;
    text-decoration: none;
  }
  .banner-code {
    position: absolute;
    right: 29px;
    bottom: 25px;
    font-size: 12px;
    font-weight: 500;
    color: var(--text-white);
  }
</style>
</head>
<body>
  <section class="hero-banner" aria-label="Velmora JESD204C IP">
    <div class="accent-band"></div>
    <div class="product-visual" role="img" aria-label="Dark circuit board module with chips, shown diagonally across the green band"></div>

    <h1 class="headline">
      <span class="product-name">JESD204C IP</span>
      <span class="tagline">Extreme Bandwidth.</span>
      <span class="tagline">Simplified Connectivity.</span>
    </h1>

    <ul class="feature-list">
      <li class="feature-item">
        <svg class="tick" viewBox="0 0 22 22" aria-hidden="true"><rect width="22" height="22" rx="4" fill="#22c03a"/><path d="M6 11.5l3.3 3.2L16 8" fill="none" stroke="#fff" stroke-width="2.2" stroke-linecap="round" stroke-linejoin="round"/></svg>
        <span>Up to <span class="highlight">32 Gbps</span> per lane performance</span>
      </li>
      <li class="feature-item">
        <svg class="tick" viewBox="0 0 22 22" aria-hidden="true"><rect width="22" height="22" rx="4" fill="#22c03a"/><path d="M6 11.5l3.3 3.2L16 8" fill="none" stroke="#fff" stroke-width="2.2" stroke-linecap="round" stroke-linejoin="round"/></svg>
        <span>Deterministic <span class="highlight">latency &amp; scalable</span> lanes</span>
      </li>
      <li class="feature-item">
        <svg class="tick" viewBox="0 0 22 22" aria-hidden="true"><rect width="22" height="22" rx="4" fill="#22c03a"/><path d="M6 11.5l3.3 3.2L16 8" fill="none" stroke="#fff" stroke-width="2.2" stroke-linecap="round" stroke-linejoin="round"/></svg>
        <span>Optimized for <span class="highlight">FPGA &amp; eFPGA architectures</span></span>
      </li>
    </ul>

    <a class="cta-button" href="#">Request IP Evaluation</a>
    <span class="banner-code">C58</span>
  </section>
</body>
</html>
```